Clean and modern business cards

Looking for an updated business card design for my dental office “corvanta dental” . Looking for a modern clean / sleek design . I’m thinking black background but open to seeing other options . One side needs to have an appointment card . Card needs to have logo, dentist name , phone, email , address . I’ve attached couple of cards I thought were cool as well as my logo
Target Market(s)
Dental patients
Industry/Entity Type
Dentistry
Contact Information for Business Card
Phone email address

```html
<!DOCTYPE html>
<html lang="en">
<head>
<meta charset="utf-8">
<title>Corvanta Dental – Business Card</title>
<link href="https://fonts.googleapis.com/css2?family=Montserrat:wght@400;500;700&display=swap" rel="stylesheet">
<style>
  :root {
    --page: #2a2a2a;
    --card: #141414;
    --accent: #8dc63f;
    --paper: #e8e8e8;
    --ink: #f2f2f2;
    --rule: #9a9a9a;
    --mark-faint: #262626;
    --highlight: #f5c400;
    --phone: #f5c400;
    --mail: #e63a2e;
    --web: #1fa3d6;
  }
  * { box-sizing: border-box; margin: 0; padding: 0; }
  html, body { width: 1200px; height: 900px; overflow: hidden; }
  body {
    background: var(--page);
    font-family: "Montserrat", Arial, sans-serif;
    display: flex;
    flex-direction: column;
    align-items: center;
    justify-content: center;
    gap: 44px;
  }
  .card {
    position: relative;
    width: 620px;
    height: 354px;
    background: var(--card);
    border-bottom: 2px solid var(--accent);
    box-shadow: 0 10px 30px rgba(0,0,0,.45);
    overflow: hidden;
  }

  /* Front */
  .brand-block {
    position: absolute;
    left: 40px; top: 137px;
    width: 250px;
    display: flex; align-items: center; justify-content: center; gap: 14px;
  }
  .brand-block .dot {
    width: 40px; height: 40px; border-radius: 50%;
    background: var(--accent);
    flex: none;
  }
  .brand-name {
    color: var(--ink);
    font-weight: 500;
    font-size: 17px;
    letter-spacing: 4px;
    line-height: 1.5;
    text-transform: uppercase;
  }
  .divider {
    position: absolute;
    left: 318px; top: 40px;
    width: 1.5px; height: 274px;
    background: var(--accent);
  }
  .contact {
    position: absolute;
    left: 350px; top: 84px;
    color: var(--ink);
  }
  .dentist-name {
    color: var(--accent);
    font-weight: 700;
    font-size: 22px;
    margin-bottom: 16px;
  }
  .address { font-size: 14px; line-height: 1.45; margin-bottom: 16px; }
  .contact-list { list-style: none; font-size: 14px; line-height: 1.75; }
  .contact-list li { display: flex; align-items: center; gap: 8px; }
  .contact-list svg { width: 13px; height: 13px; flex: none; }

  /* Back */
  .back-mark {
    position: absolute;
    right: 36px; top: 26px;
    display: flex; align-items: center; gap: 12px;
  }
  .back-mark .dot {
    width: 44px; height: 44px; border-radius: 50%;
    background: var(--mark-faint);
  }
  .back-mark .brand-name { color: var(--mark-faint); font-size: 20px; letter-spacing: 3px; font-weight: 700; }
  .appointment {
    position: absolute;
    left: 0; top: 100px;
    width: 520px; height: 130px;
    background: var(--paper);
    padding: 26px 40px 0 40px;
  }
  .field {
    display: flex; align-items: flex-end; gap: 6px;
    font-size: 15px; color: #222;
    height: 40px;
  }
  .field .line { flex: 1; border-bottom: 1px solid var(--rule); margin-bottom: 4px; }
  .notice {
    position: absolute;
    left: 40px; top: 256px;
    width: 540px;
    color: var(--ink);
    font-size: 15px;
    line-height: 1.5;
  }
  .notice strong { color: var(--highlight); font-weight: 700; }
</style>
</head>
<body>

  <section class="card card-front">
    <div class="brand-block">
      <span class="dot"></span>
      <span class="brand-name">Corvanta<br>Dental</span>
    </div>
    <div class="divider"></div>
    <div class="contact">
      <h1 class="dentist-name">Dr. Lev Orlanski</h1>
      <p class="address">2480 Calloway Ave<br>Winnipeg, MB</p>
      <ul class="contact-list">
        <li>
          <svg viewBox="0 0 16 16" aria-hidden="true"><path fill="var(--phone)" d="M3.5 1 6 1.5 7 5 5.3 6.3c.8 1.8 2.3 3.3 4.2 4.2L10.8 9l3.5 1 .5 2.5-1.8 1.8C7.5 14 2 8.5 1.7 2.8z"/></svg>
          (204)-555-0172
        </li>
        <li>
          <svg viewBox="0 0 16 16" aria-hidden="true"><rect x="1" y="3" width="14" height="10" fill="var(--mail)"/><path d="M1 3l7 6 7-6" fill="none" stroke="var(--card)" stroke-width="1.4"/></svg>
          hello@corvantawpg.ca
        </li>
        <li>
          <svg viewBox="0 0 16 16" aria-hidden="true"><circle cx="8" cy="8" r="7" fill="var(--web)"/><path d="M1 8h14M8 1c-3 3.5-3 10.5 0 14M8 1c3 3.5 3 10.5 0 14" fill="none" stroke="var(--card)" stroke-width="1"/></svg>
          corvantawpg.ca
        </li>
      </ul>
    </div>
  </section>

  <section class="card card-back">
    <div class="back-mark">
      <span class="dot"></span>
      <span class="brand-name">Corvanta Dental</span>
    </div>
    <div class="appointment">
      <div class="field"><span>Date</span><span class="line"></span></div>
      <div class="field"><span>Time</span><span class="line"></span></div>
    </div>
    <p class="notice">To cancel or reschedule please notify us at least<br><strong>48</strong> hours prior to your scheduled appointment</p>
  </section>

</body>
</html>
```